Business Goals Posters for display within company office and factory.

We have three (3) high level business goals we want to display in the office and factory areas of the business.

1. Under the heading of "QUALITY"
"We will have pride and ownership of every product and service delivered to our customers."

2. Under the heading of "PRODUCTIVITY"
"We will put the customer's expectations first and ensure our team is empowered to do so."

3. Under the heading of "SAFETY"
"We will shift our culture to ensure safety is our first thought on every job."

We would like a matching set of posters with these three headings and statements with a background suitable for display in a business environment. The posters will be displayed in sizes from A4 and A2.
The company's logo is Red and Black (see attachment) .
We make Electric and Hydraulic power packs for industrial market.
our website will give you an idea of what we do www.tarnwickdrives.com.au

Industry/Entity Type

Power Generation

Colors

Designer to choose colors to be used in the design.

Requirements
Must have
• The posters must use the exact text provided and have the headings listed.
• the three posters must have a common theme. they can be different in back ground but when side by side must look like a set.
• Be suitable for display as A4 and as A2.
Nice to have
• The text needs the be the star, the background needs to draw attention to the poster and the text with out over powering it,
Should not have
• not have photo's of generators or equipment as backgrounds

```html
<!DOCTYPE html>
<html lang="en">
<head>
<meta charset="utf-8">
<title>Tarnwick Drives – Business Goals Posters</title>
<link rel="stylesheet" href="https://fonts.googleapis.com/css2?family=Russo+One&family=Aldrich&display=swap">
<style>
  :root {
    --stage: #6b6b6b;
    --stage-light: #8a8a8a;
    --quality-base: #5e4a78;
    --quality-glow: #8a76a6;
    --safety-base: #66723f;
    --safety-glow: #a3ac84;
    --productivity-base: #5e3338;
    --productivity-glow: #a06e72;
    --ink-white: #ffffff;
    --ink-grey: #c9c9c9;
    --brand-red: #e3262b;
    --brand-black: #111111;
    --corner-white: #ffffff;
  }
  * { box-sizing: border-box; margin: 0; padding: 0; }
  html, body { width: 1200px; height: 600px; overflow: hidden; }
  body {
    background: radial-gradient(ellipse at 50% 40%, var(--stage-light), var(--stage) 75%);
    font-family: "Aldrich", sans-serif;
    position: relative;
  }
  .poster {
    position: absolute;
    top: 78px;
    width: 316px;
    height: 444px;
    overflow: hidden;
  }
  .poster--quality { left: 90px; background: radial-gradient(circle at 45% 48%, var(--quality-glow), var(--quality-base) 70%); }
  .poster--safety { left: 432px; background: radial-gradient(circle at 45% 40%, var(--safety-glow), var(--safety-base) 70%); }
  .poster--productivity { left: 778px; background: radial-gradient(circle at 30% 55%, var(--productivity-glow), var(--productivity-base) 70%); }

  .backdrop-word {
    position: absolute;
    font-family: "Russo One", sans-serif;
    font-size: 150px;
    line-height: 1;
    color: rgba(30, 20, 35, 0.28);
    white-space: nowrap;
    transform: rotate(-22deg);
    transform-origin: left top;
  }
  .backdrop-word--top { left: -30px; top: 95px; }
  .backdrop-word--bottom { left: -20px; top: 430px; }

  .heading {
    position: absolute;
    left: 0; right: 0;
    top: 138px;
    text-align: center;
    font-family: "Russo One", sans-serif;
    font-size: 50px;
    line-height: 1;
    letter-spacing: 1px;
    color: var(--ink-white);
    text-shadow: 3px 4px 0 rgba(0, 0, 0, 0.35);
  }
  .poster--productivity .heading { font-size: 37px; top: 146px; }
  .heading .accent {
    background: linear-gradient(160deg, var(--ink-grey) 0 38%, var(--brand-red) 38% 100%);
    -webkit-background-clip: text;
    background-clip: text;
    color: transparent;
  }
  .heading .shade {
    background: linear-gradient(160deg, var(--ink-white) 0 50%, var(--ink-grey) 50% 100%);
    -webkit-background-clip: text;
    background-clip: text;
    color: transparent;
  }
  .statement {
    position: absolute;
    left: 10px; right: 10px;
    top: 203px;
    text-align: center;
    font-size: 14.5px;
    line-height: 20px;
    letter-spacing: 0.6px;
    text-transform: uppercase;
    color: var(--ink-white);
  }
  .corner {
    position: absolute;
    left: 0; bottom: 0;
    width: 316px; height: 104px;
  }
  .brand {
    position: absolute;
    right: 20px;
    bottom: 22px;
    display: flex;
    align-items: center;
    gap: 6px;
    font-size: 14px;
    color: var(--brand-black);
  }
  .brand__mark {
    width: 12px; height: 12px;
    background: var(--brand-red);
  }
</style>
</head>
<body>

<section class="poster poster--quality">
  <div class="backdrop-word backdrop-word--top" aria-hidden="true">QUALITY</div>
  <div class="backdrop-word backdrop-word--bottom" aria-hidden="true">QUALITY</div>
  <h1 class="heading">QU<span class="shade">A</span><span class="accent">LI</span>TY</h1>
  <p class="statement">We will have pride and ownership of every product and service delivered to our customers</p>
  <svg class="corner" viewBox="0 0 316 104" aria-hidden="true"><polygon points="0,104 316,0 316,104" fill="var(--corner-white)"/></svg>
  <div class="brand"><span class="brand__mark"></span>Tarnwick Drives</div>
</section>

<section class="poster poster--safety">
  <div class="backdrop-word backdrop-word--top" aria-hidden="true">SAFETY</div>
  <div class="backdrop-word backdrop-word--bottom" aria-hidden="true">SAFETY</div>
  <h1 class="heading"><span class="shade">S</span>AF<span class="accent">E</span>TY</h1>
  <p class="statement">We will shift our culture to ensure safety is our first thought on every job</p>
  <svg class="corner" viewBox="0 0 316 104" aria-hidden="true"><polygon points="0,104 316,0 316,104" fill="var(--corner-white)"/></svg>
  <div class="brand"><span class="brand__mark"></span>Tarnwick Drives</div>
</section>

<section class="poster poster--productivity">
  <div class="backdrop-word backdrop-word--top" aria-hidden="true">PRODUCTIVITY</div>
  <div class="backdrop-word backdrop-word--bottom" aria-hidden="true">PRODUCTIVITY</div>
  <h1 class="heading">PRO<span class="shade">D</span><span class="accent">UCTI</span>VITY</h1>
  <p class="statement">We will put the customer's expectations first and ensure our team is empowered to do so</p>
  <svg class="corner" viewBox="0 0 316 104" aria-hidden="true"><polygon points="0,104 316,0 316,104" fill="var(--corner-white)"/></svg>
  <div class="brand"><span class="brand__mark"></span>Tarnwick Drives</div>
</section>

</body>
</html>
```